Poster Design Project

About Us
Brimco is a company that specializes in providing communication solutions to the travel market. Our simple vision of “every hotel should have a mobile phone in the guest rooms”, led us to develop a path breaking cost effective mobile phone. With full integration capabilities with the hotels property management system, location based marketing, user locator and other features, this product is unique in addressing the hospitality segment.
Product Placement
The Brimco mobile will be placed in the hotel room on an A4 Sized transparent stand (the transparent stand is attached for your reference. If you notice, the phone will be placed in the jacket on the bottom left and in another jacket on the bottom right will be the brochure. So effectively, the design space available on the A4 brochure is only 60% of the space). The designed poster that we wish designed will be inserted in the A4 sized acrylic stand. The stand would typically be on the bedside table or on the study table of the hotel room. The A4 design should be bright and vibrant in keeping with our logo colors.
Attached is our logo. Also attached is the symbol of our phone that could be used innovatively on the brochure if you think it helps.
Attached is the content for the poster.
Reason: Feedback from the management team got delayed, hence the extension. Thanks
Reason: The delay is in the content finalization.

```html
<!DOCTYPE html>
<html lang="en">
<head>
<meta charset="utf-8">
<title>Brimco Hotel Phone Poster</title>
<link rel="stylesheet" href="https://fonts.googleapis.com/css2?family=Open+Sans:wght@700;800&family=Bree+Serif&family=Chewy&display=swap">
<style>
  :root {
    --orange: #f7941d;
    --orange-light: #fbb040;
    --ink: #1d1b1a;
    --band-dark: #231f20;
    --paper: #ffffff;
    --backdrop: #ece8e2;
    --rim: #8a8a8a;
  }
  * { margin: 0; padding: 0; box-sizing: border-box; }
  html, body {
    width: 878px;
    height: 1200px;
    overflow: hidden;
    background: var(--backdrop);
  }
  .poster {
    position: absolute;
    left: 28px;
    top: 20px;
    width: 822px;
    height: 1160px;
    background: var(--orange);
    overflow: hidden;
    box-shadow: 0 4px 14px rgba(0,0,0,0.25);
    font-family: "Open Sans", Arial, sans-serif;
  }
  .offer-backdrop {
    position: absolute;
    left: 0; top: 0;
    width: 822px; height: 483px;
    background: linear-gradient(180deg, #f6a445 0%, #e99a3c 55%, #d98b32 100%);
  }
  .guest-photo {
    position: absolute;
    left: 557px; top: 210px;
    width: 265px; height: 273px;
    background: linear-gradient(160deg, #c7424b 0%, #a8353d 45%, #5b3a36 100%);
  }
  .header-shape {
    position: absolute;
    left: 0; top: 0;
  }
  .brand-name {
    position: absolute;
    left: 30px; top: 14px;
    font-weight: 800;
    font-size: 96px;
    line-height: 1;
    color: var(--orange);
    letter-spacing: -1px;
  }
  .brand-mark {
    position: absolute;
    left: 540px; top: 6px;
    width: 266px; height: 266px;
    border-radius: 50%;
    background: var(--orange);
    border: 6px solid var(--rim);
  }
  .offer-list {
    position: absolute;
    left: 0; top: 155px;
    width: 512px;
    text-align: center;
    color: var(--ink);
    font-weight: 700;
    font-size: 22px;
    line-height: 30px;
    list-style: none;
    white-space: nowrap;
  }
  .offer-list .plus { font-size: 16px; line-height: 24px; }
  .offer-price {
    position: absolute;
    left: 36px; top: 378px;
    font-weight: 800;
    font-size: 66px;
    line-height: 1;
    color: #000;
  }
  .feature-band {
    position: absolute;
    left: 0; top: 483px;
    width: 822px; height: 111px;
    background: var(--paper);
  }
  .feature-row {
    position: absolute;
    left: 0; width: 822px;
    height: 32px;
    display: flex;
    align-items: center;
    justify-content: center;
  }
  .feature-row .dash-fill {
    flex: 1;
    height: 6px;
    margin: 0 14px;
    background: repeating-linear-gradient(90deg, var(--orange) 0 30px, transparent 30px 52px);
  }
  .feature-row .feature {
    font-family: "Chewy", "Comic Sans MS", cursive;
    font-size: 25px;
    color: var(--orange);
    -webkit-text-stroke: 1.5px #6b3a06;
    paint-order: stroke fill;
    white-space: nowrap;
  }
  .feature-row.r1 { top: 6px; }
  .feature-row.r2 { top: 39px; }
  .feature-row.r3 { top: 72px; }
  .cta-band {
    position: absolute;
    left: 0; top: 594px;
    width: 822px; height: 102px;
    background: var(--band-dark);
    text-align: center;
    font-family: "Bree Serif", Georgia, serif;
    color: var(--orange);
  }
  .cta-band .cta-brand {
    display: block;
    margin-top: 8px;
    font-size: 38px;
    line-height: 44px;
  }
  .cta-band .cta-line {
    display: block;
    font-size: 25px;
    line-height: 30px;
    padding-left: 20px;
  }
  .cta-arrow {
    position: absolute;
    left: 26px; top: 612px;
  }
  .phone-pocket {
    position: absolute;
    left: 0; top: 696px;
    width: 822px; height: 464px;
    background: radial-gradient(ellipse at 50% 0%, #fbb040 0%, #f7941d 55%, #f08a14 100%);
  }
</style>
</head>
<body>
  <main class="poster">
    <div class="offer-backdrop" role="img" aria-label="Faded orange-toned city rooftops behind the offer"></div>
    <div class="guest-photo" role="img" aria-label="Photo of a smiling traveller with raised arms among red autumn leaves"></div>

    <svg class="header-shape" width="822" height="320" viewBox="0 0 822 320" aria-hidden="true">
      <path d="M0 0 H822 V218 C790 240 760 292 672 292 C610 292 565 250 540 200 C522 165 510 143 470 143 H0 Z" fill="#ffffff"/>
      <path d="M0 143 H470 C510 143 522 165 540 200 C565 250 610 292 672 292 C760 292 790 240 822 218" fill="none" stroke="#231f20" stroke-width="4"/>
    </svg>

    <h1 class="brand-name">Brimco</h1>
    <div class="brand-mark" aria-hidden="true"></div>

    <ul class="offer-list">
      <li>SAVE 80% on international roaming</li>
      <li class="plus">+</li>
      <li>Get a LOCAL number</li>
      <li class="plus">+</li>
      <li>60 FREE minutes of international Calls</li>
      <li class="plus">+</li>
      <li>60 FREE minutes of local calls</li>
    </ul>
    <p class="offer-price">= 499 BHT</p>

    <section class="feature-band">
      <div class="feature-row r1"><span class="dash-fill"></span><span class="feature">Itemized bill on checkout</span><span class="dash-fill"></span></div>
      <div class="feature-row r2"><span class="dash-fill"></span><span class="feature">Flexible tariff plans to choose from</span><span class="dash-fill"></span></div>
      <div class="feature-row r3"><span class="dash-fill"></span><span class="feature">Excellent call quality</span><span class="dash-fill"></span></div>
    </section>

    <section class="cta-band">
      <span class="cta-brand">Brimco.</span>
      <span class="cta-line">Pick up this phone NOW, to keep talking.</span>
    </section>
    <svg class="cta-arrow" width="150" height="80" viewBox="0 0 150 80" aria-hidden="true">
      <defs>
        <linearGradient id="arrowFade" x1="1" y1="0" x2="0" y2="0">
          <stop offset="0" stop-color="#f7941d" stop-opacity="0"/>
          <stop offset="0.5" stop-color="#f7941d"/>
          <stop offset="1" stop-color="#fbb040"/>
        </linearGradient>
      </defs>
      <path d="M150 6 H44 C34 6 30 12 30 22 V46 H10 L38 78 L66 46 H46 V26 C46 22 48 20 52 20 H150 Z" fill="url(#arrowFade)"/>
    </svg>

    <div class="phone-pocket" role="img" aria-label="Orange sunburst rays radiating from the top centre, where the phone sits"></div>
  </main>
</body>
</html>
```